Bright Harbor Counseling Letterhead for hip modern business

I would like some ombre use of the colors in the logo hip letterhead that incorporates logo colors and feel, needs to connect with young professionals and college students. i need to be able to write letters to schools to excuse absences as well. i like color blocks on one side preferably using colors from the attached logo design.

Target Market(s)

high income young people, young adults and college students

Industry/Entity Type

mental health

Font styles to use
Serif
Sans Serif

Colors
0054AA
0677BA
7BADD7
CADEEF
E8F1F8
0094D4
00A9DD
6FCCEA
C7EBF8
E9F6FB
00AB8E
00BBA5
67D7C9
C6EFE9
E9F9F6
59FF00
82FF00
B8FF75
E3FFCB
F4FFEA
A7469A
B969AE
D3A5CF
EDDBEB
F8F0F9
6B429C
8869AF
B7A5CE
E3DAEB
F3F0F8

Requirements
Must have
• a modern hip feel, somewhat color

```html
<!DOCTYPE html>
<html lang="en">
<head>
<meta charset="utf-8">
<title>Bright Harbor Counseling Letterhead</title>
<link rel="stylesheet" href="https://fonts.googleapis.com/css2?family=Tinos:wght@400;700&display=swap">
<style>
  :root {
    --ink: #111111;
    --violet-deep: #4a22ff;
    --violet-mid: #7f5bff;
    --violet-soft: #b9a8f9;
    --violet-pale: #e8def9;
    --violet-mist: #f5f2fd;
    --curve-light: #b3a3fb;
    --paper: #ffffff;
    --sign-fill: #ececf2;
  }
  * { margin: 0; padding: 0; box-sizing: border-box; }
  html, body { width: 927px; height: 1200px; overflow: hidden; background: var(--paper); }
  body { font-family: "Tinos", "Times New Roman", serif; color: var(--ink); }
  .letterhead { position: relative; width: 927px; height: 1200px; background: var(--paper); overflow: hidden; }

  .corner-sweep { position: absolute; left: 0; top: 0; }

  .color-blocks { position: absolute; right: 0; top: 0; width: 54px; height: 1200px; display: flex; flex-direction: column; }
  .color-blocks span { flex: 1; }
  .block-1 { background: var(--violet-deep); }
  .block-2 { background: var(--violet-mid); }
  .block-3 { background: var(--violet-soft); }
  .block-4 { background: var(--violet-pale); }
  .block-5 { background: var(--violet-mist); }

  .brand { position: absolute; left: 103px; top: 162px; width: 250px; font-weight: 400; color: var(--ink); }
  .brand-dot { position: absolute; left: 262px; top: -60px; width: 56px; height: 56px; border-radius: 50%; background: var(--violet-mid); }
  .brand-name { display: block; font-size: 40px; line-height: 48px; }
  .brand-sub { display: block; font-size: 22px; line-height: 26px; letter-spacing: 3px; text-align: right; }

  .sender { position: absolute; left: 102px; top: 285px; }
  .sender-name { font-size: 28px; font-weight: 700; line-height: 30px; }
  .sender-position { font-size: 17.5px; line-height: 22px; }
  .sender-details { margin-top: 18px; font-size: 15px; line-height: 18.3px; }

  .letter-body { position: absolute; left: 102px; top: 455px; width: 720px; font-size: 14.6px; line-height: 18.2px; }
  .letter-body p + p { margin-top: 31px; }

  .closing { position: absolute; left: 102px; top: 900px; font-size: 17px; }
  .signature-area { display: block; margin: 8px 0 0 -8px; width: 141px; height: 44px; background: var(--sign-fill); border-radius: 3px; }
  .closing-position { margin-top: 6px; }

  .contact-bar { position: absolute; left: 95px; top: 1132px; display: flex; gap: 0; }
  .contact-item { width: 187px; display: flex; align-items: center; gap: 5px; font-size: 14.6px; font-weight: 700; }
  .contact-icon { width: 27px; height: 27px; border-radius: 4px; background: var(--violet-deep); display: flex; align-items: center; justify-content: center; }
</style>
</head>
<body>
<main class="letterhead">
  <svg class="corner-sweep" width="360" height="420" viewBox="0 0 360 420" aria-hidden="true">
    <defs>
      <linearGradient id="sweepGradient" x1="0" y1="0" x2="0.3" y2="1">
        <stop offset="0" stop-color="#4a22ff"/>
        <stop offset="1" stop-color="#8a6bff"/>
      </linearGradient>
    </defs>
    <path d="M0,0 L355,0 C170,20 25,170 0,413 Z" fill="var(--curve-light)"/>
    <path d="M0,0 L300,0 C150,25 25,140 0,312 Z" fill="url(#sweepGradient)"/>
  </svg>

  <div class="color-blocks" aria-hidden="true">
    <span class="block-1"></span><span class="block-2"></span><span class="block-3"></span><span class="block-4"></span><span class="block-5"></span>
  </div>

  <div class="brand">
    <span class="brand-dot" aria-hidden="true"></span>
    <span class="brand-name">Bright Harbor</span>
    <span class="brand-sub">Counseling</span>
  </div>

  <section class="sender">
    <h1 class="sender-name">NAME SURNAME</h1>
    <p class="sender-position">POSITION</p>
    <p class="sender-details">ADDRESS:<br>EMAIL:<br>CONTACT NO:</p>
  </section>

  <section class="letter-body">
    <p>Ne porepra ectior at ent esti dolorrovides es re pero conecusam quoditae necte volum et, inveles ectaquas evel esequo volorum ipitia que ma verspero dolorporem harupta aspis aspitatem num sunt.<br>Aquibust antio dolorere porum as iur, te eos ut fuga. Itat ella sam sequi coris elita qui accusda nonet fugia velignam nonse volores quamenis explique volupta ssequatur magnam ipsandiae si officil ium quatatet quos et eum que illoreperis dolor audamus exceatiis ea plia earci aut que ni aped maios cum escipsum faccabo. Id ut qui aperio tem experumquos eos simagnitas rendand</p>
    <p>Ne porepra ectior at ent esti dolorrovides es re pero conecusam quoditae necte volum et, inveles ectaquas evel esequo volorum ipitia que ma verspero dolorporem harupta aspis aspitatem num sunt.<br>Aquibust antio dolorere porum as iur, te eos ut fuga. Itat ella sam sequi coris elita qui accusda nonet fugia velignam nonse volores quamenis explique volupta ssequatur magnam ipsandiae si officil ium quatatet quos et eum que illoreperis dolor audamus exceatiis ea plia earci aut que ni aped maios cum escipsum faccabo. Id ut qui aperio tem experumquos eos simagnitas rendand</p>
    <p>Ne porepra ectior at ent esti dolorrovides es re pero conecusam quoditae necte volum et, inveles ectaquas evel esequo volorum ipitia que ma verspero dolorporem harupta aspis aspitatem num sunt.<br>Aquibust antio dolorere porum as iur, te eos ut fuga. Itat ella sam sequi coris elita qui accusda nonet fugia velignam nonse volores quamenis explique volupta ssequatur magnam ipsandiae si officil ium quatatet quos et eum que illoreperis dolor audamus exceatiis ea plia earci aut que ni aped maios cum escipsum faccabo. Id ut qui aperio tem experumquos eos simagnitas rendand</p>
  </section>

  <section class="closing">
    <p>Regards,</p>
    <span class="signature-area" role="img" aria-label="Handwritten signature"></span>
    <p class="closing-position">Position</p>
  </section>

  <footer class="contact-bar">
    <div class="contact-item">
      <span class="contact-icon"><svg width="15" height="15" viewBox="0 0 24 24" aria-hidden="true"><path fill="#fff" d="M6.6 10.8a15.1 15.1 0 0 0 6.6 6.6l2.2-2.2c.3-.3.7-.4 1-.2 1.1.4 2.3.6 3.6.6.6 0 1 .4 1 1V20c0 .6-.4 1-1 1A17 17 0 0 1 3 4c0-.6.4-1 1-1h3.5c.6 0 1 .4 1 1 0 1.3.2 2.5.6 3.6.1.3 0 .7-.2 1z"/></svg></span>
      Volorumqui ullatque
    </div>
    <div class="contact-item">
      <span class="contact-icon"><svg width="15" height="15" viewBox="0 0 24 24" aria-hidden="true"><rect x="3" y="5" width="18" height="14" rx="1" fill="none" stroke="#fff" stroke-width="2"/><path d="M3 6l9 7 9-7" fill="none" stroke="#fff" stroke-width="2"/></svg></span>
      Volorumqui ullatque
    </div>
    <div class="contact-item">
      <span class="contact-icon"><svg width="16" height="16" viewBox="0 0 24 24" aria-hidden="true"><g fill="none" stroke="#fff" stroke-width="1.8"><circle cx="12" cy="12" r="9"/><ellipse cx="12" cy="12" rx="4" ry="9"/><path d="M3 12h18M5 7h14M5 17h14"/></g></svg></span>
      Volorumqui ullatque
    </div>
    <div class="contact-item">
      <span class="contact-icon"><svg width="15" height="15" viewBox="0 0 24 24" aria-hidden="true"><path fill="#fff" d="M12 2a7 7 0 0 0-7 7c0 5 7 13 7 13s7-8 7-13a7 7 0 0 0-7-7zm0 9.5A2.5 2.5 0 1 1 12 6.5a2.5 2.5 0 0 1 0 5z"/></svg></span>
      Volorumqui ullatque
    </div>
  </footer>
</main>
</body>
</html>
```